Deactivated Coal-Fired Power Plant to be redeveloped into a Green Energy Campus.

Want a striking business card statement that introduces our concept project to provide economic and community recovery to a former rural coal community in western PA.
Essentially 12 project representatives that will lead both the demolition of an existing power plant and the redevelopment to a new Green energy site.
Business Card should reflect our effort.
We are open to ideas.

Target Market(s)

Energy and Power Generation industries

Industry/Entity Type

Power Generation and Data Centers

Contact Information for Business Card

Included in uploaded materials

Font styles to use
Sans Serif
Other font styles liked:
• Arial, Calibri

Requirements
Must have
• Multiple colors

```html
<!DOCTYPE html>
<html lang="en">
<head>
<meta charset="utf-8">
<title>Larkfield Renewal – Business Card</title>
<link href="https://fonts.googleapis.com/css2?family=Arimo:wght@400;700&display=swap" rel="stylesheet">
<style>
  :root {
    --stage: #d9d9d9;
    --paper: #ffffff;
    --ink: #0b0b0b;
    --green: #17944a;
    --text-light: #f2f2f2;
    --rule: rgba(23, 148, 74, 0.55);
  }
  * { box-sizing: border-box; margin: 0; padding: 0; }
  html, body {
    width: 1200px;
    height: 900px;
    overflow: hidden;
    background: var(--stage);
    font-family: "Arimo", Arial, sans-serif;
  }
  .stage {
    position: relative;
    width: 1200px;
    height: 900px;
    display: flex;
    justify-content: center;
    align-items: center;
    gap: 70px;
  }
  .card {
    position: relative;
    width: 330px;
    height: 578px;
    background: var(--paper);
    overflow: hidden;
    box-shadow: 0 10px 28px rgba(0, 0, 0, 0.18);
  }
  .brand {
    position: absolute;
    left: 0;
    right: 0;
    display: flex;
    align-items: center;
    justify-content: center;
    gap: 10px;
    color: var(--ink);
    font-weight: 700;
    letter-spacing: 0.5px;
  }
  .brand-dot {
    border-radius: 50%;
    background: var(--green);
    flex: none;
  }
  .card--front .brand { top: 70px; font-size: 24px; }
  .card--front .brand-dot { width: 26px; height: 26px; }
  .card--back .brand { top: 120px; font-size: 30px; }
  .card--back .brand-dot { width: 34px; height: 34px; }

  .skyline {
    position: absolute;
    left: 0;
    right: 0;
    bottom: 0;
    background: var(--ink);
  }
  .card--front .skyline { top: 250px; }
  .card--back .skyline { top: 370px; }

  .contact {
    position: absolute;
    left: 0;
    right: 0;
    top: 340px;
    text-align: center;
    color: var(--text-light);
    font-size: 12.5px;
    line-height: 1.35;
  }
  .contact-name {
    color: var(--green);
    font-weight: 700;
    font-size: 18px;
  }
  .contact-role { margin-bottom: 14px; }
  .contact-label { color: var(--green); margin-right: 3px; }
  .contact-rule {
    width: 190px;
    height: 1px;
    margin: 12px auto;
    background: var(--rule);
  }
  .contact-line { margin-bottom: 6px; }
</style>
</head>
<body>
<main class="stage">
  <article class="card card--front">
    <div class="brand"><span class="brand-dot"></span>Larkfield Renewal</div>
    <div class="skyline" role="img" aria-label="Silhouette of a power plant skyline with smokestacks and cooling towers"></div>
    <div class="contact">
      <p class="contact-name">Daniel Harrow</p>
      <p class="contact-role">Chief Operating Officer</p>
      <p class="contact-line"><span class="contact-label">M.</span>555.014.2280</p>
      <p class="contact-line"><span class="contact-label">E.</span>dharrow@larkfieldrenewal</p>
      <div class="contact-rule"></div>
      <p class="contact-line"><span class="contact-label">P.</span>555.019.4400</p>
      <p>Larkfield</p>
      <p>Pennsylvania, United States</p>
    </div>
  </article>

  <article class="card card--back">
    <div class="brand"><span class="brand-dot"></span>Larkfield Renewal</div>
    <div class="skyline" role="img" aria-label="Silhouette of a power plant skyline with smokestacks and cooling towers"></div>
  </article>
</main>
</body>
</html>
```